Speisekarten-Design für gehobenes italienisches Restaurant
Zielgruppe
Wir sind ein gehobenes italienisches Restaurant und suchen ein neues Design für unsere Speisekarte. Wir haben ein eher älteres Publikum.
Aufgabenstellung
Wir möchten eine elegantes modernes Design. Einzelseiten im A4 Format.

```html
<!DOCTYPE html>
<html lang="de">
<head>
<meta charset="utf-8">
<title>Casa Vittoria – Speisekarte</title>
<link rel="stylesheet" href="https://fonts.googleapis.com/css2?family=Montserrat:wght@300;400;600;700&family=Pinyon+Script&display=swap">
<style>
:root{
  --bg:#efeeec;
  --paper:#ffffff;
  --ink:#111111;
  --text:#333333;
  --muted:#5e5e5e;
  --soft:#777777;
  --rule:#444444;
  --accent:#e0523f;
  --brand:#dcc6c2;
  --green:#1f8a3c;
  --red:#e1251b;
}
*{margin:0;padding:0;box-sizing:border-box}
html,body{width:1200px;height:675px;overflow:hidden;background:var(--bg)}
body{position:relative;font-family:'Montserrat',sans-serif;color:var(--text)}
.page{position:absolute;width:372px;height:526px;background:var(--paper);box-shadow:0 2px 10px rgba(0,0,0,.12)}
.page--aperitifs{left:20px;top:36px}
.page--food{left:414px;top:74px}
.page--drinks{left:808px;top:36px}
.abs{position:absolute}

/* section titles */
.title-block{position:absolute;left:98px;width:177px;height:51px;border-top:1px solid var(--rule);border-bottom:1px solid var(--rule)}
.title{position:absolute;left:0;right:0;bottom:6px;text-align:center;font-weight:300;font-size:15px;letter-spacing:.5px;color:var(--ink);white-space:nowrap}
.title .initial{font-family:'Pinyon Script',cursive;font-size:50px;line-height:0;margin-right:-6px;vertical-align:-2px}

.script-head{position:absolute;font-family:'Pinyon Script',cursive;font-size:19px;color:var(--ink);text-shadow:2px 3px 3px rgba(0,0,0,.25);white-space:nowrap}

/* menu items */
.item{position:absolute}
.item .name{font-size:10px;font-weight:400;color:var(--ink);line-height:12px;white-space:nowrap}
.item .name sup,.row sup{font-size:5px;vertical-align:5px}
.item .desc{font-size:6.3px;line-height:7.4px;color:var(--muted)}
.vol{font-size:4.5px;color:var(--accent);margin:0 6px}
.price{font-weight:700;font-size:6.5px;color:var(--ink)}
.item--left .price{position:absolute;left:96px;bottom:0}
.item--left .vol{position:absolute;left:72px;bottom:1px;margin:0}
.item--right{right:22px;text-align:right}
.item--dish .price{position:absolute;right:0;top:12px}

.col-rule{position:absolute;left:174px;top:211px;width:1px;height:237px;background:#999}
.label-bold{position:absolute;font-weight:700;font-size:7px;color:var(--ink);text-shadow:1px 2px 2px rgba(0,0,0,.2)}

/* spirits box */
.spirit-box{position:absolute;left:21px;top:134px;width:331px;height:31px;border:1px solid #777}
.spirit{position:absolute;top:3px;font-family:'Montserrat',sans-serif}
.spirit .sname{font-size:8.5px;color:var(--ink)}
.spirit .sdesc{font-size:5.3px;color:var(--ink);margin-top:2px;white-space:nowrap}

/* drink rows */
.row{position:absolute;left:0;right:0;height:12px}
.row span{position:absolute;top:0;white-space:nowrap}
.row .dname{font-size:10px;font-weight:300;color:var(--muted)}
.row .p{font-size:8px;font-weight:700;color:var(--ink);top:2px}
.vol-head{position:absolute;font-size:6px;color:var(--soft)}

/* image areas */
.photo{position:absolute}
.photo--soup{left:224px;top:69px;width:66px;height:44px;border-radius:50%;background:radial-gradient(circle at 50% 40%,#e8622e 0 38%,#b33a22 40% 52%,#c7302a 54% 70%,rgba(255,255,255,0) 72%)}
.photo--caprese{left:55px;top:269px;width:69px;height:35px;border-radius:50%;background:radial-gradient(ellipse at 50% 50%,#d8352b 0 35%,#f2f2ee 37% 48%,#e9e9e6 50% 70%,rgba(255,255,255,0) 72%)}

/* brand mark */
.brand{position:absolute;left:258px;width:96px;text-align:center;font-size:14px;font-weight:400;color:var(--brand);white-space:nowrap}

/* tricolore band */
.tricolore{position:absolute;left:66px;width:241px;height:8px;display:flex;border:1px solid #555}
.tricolore i{flex:1}
.tricolore .g{background:var(--green)}
.tricolore .w{background:#fff}
.tricolore .r{background:var(--red)}
</style>
</head>
<body>

<!-- Aperitif page -->
<section class="page page--aperitifs">
  <div class="title-block" style="top:67px"><h2 class="title"><span class="initial">A</span>peritifs</h2></div>

  <div class="spirit-box">
    <div class="spirit" style="left:2px"><div class="sname">Sherry</div><div class="sdesc">trocken | medium | süß <span class="vol" style="margin:0 4px">5cl</span> 5.90</div></div>
    <div class="spirit" style="left:0;right:0;text-align:center"><div class="sname">Vermello</div><div class="sdesc">bianco | rosso <span class="vol" style="margin:0 4px">5cl</span> 6.00</div></div>
    <div class="spirit" style="right:3px;text-align:right"><div class="sname">Camporosso</div><div class="sdesc">bianco | rosso <span class="vol" style="margin:0 4px">5cl</span> 6.00</div></div>
  </div>

  <div class="col-rule"></div>

  <div class="item item--left" style="left:21px;top:218px;width:150px"><div class="name">Hugo</div><p class="desc">Prosecco Spumante, Holunderblütensirup, Soda,<br>Pfefferminz</p><span class="vol">0,2l</span><span class="price">7.90</span></div>
  <div class="item item--left" style="left:21px;top:252px;width:150px"><div class="name">Black Hugo</div><p class="desc">Prosecco Spumante, Holunderblütensirup, Soda,<br>Pfefferminz</p><span class="vol">0,2l</span><span class="price">7.90</span></div>
  <div class="item item--left" style="left:21px;top:286px;width:150px"><div class="name">Apertino Spritz</div><p class="desc">Prosecco Spumante, Apertino, Soda<br>Orangenscheibe</p><span class="vol">0,2l</span><span class="price">7.90</span></div>
  <div class="item item--left" style="left:21px;top:320px;width:150px"><div class="name">Limoncello Spritz</div><p class="desc">Prosecco Spumante, Limoncello, Soda,<br>Zitrone</p><span class="vol">0,2l</span><span class="price">7.90</span></div>
  <div class="item item--left" style="left:21px;top:354px;width:150px"><div class="name">Lisette Wild Berry</div><p class="desc">Lisette, Prosecco Spumante, Dark Wild Berry,<br>Beeren, Pfefferminz</p><span class="vol">0,2l</span><span class="price">8.90</span></div>
  <div class="item item--left" style="left:21px;top:388px;width:150px"><div class="name">Lavendel Spritz</div><p class="desc">Lavendelsirup, Prosecco Spumante, Soda,<br>Zitrone</p><span class="vol">0,2l</span><span class="price">8.90</span></div>
  <div class="item item--left" style="left:21px;top:422px;width:150px"><div class="name">Moscow Mule</div><p class="desc">Nordstern Vodka, Limettensaft, Ginger Beer,<br>Ingwer Pfefferminz</p><span class="vol">0,2l</span><span class="price">8.90</span></div>

  <div class="item item--right" style="top:220px"><div class="name">Espresso Martini</div><p class="desc">Espresso Shot, Nordstern Vodka,<br>Cafetta Kaffee Likör, Creamor <span class="price" style="margin-left:4px">10.90</span></p></div>
  <div class="item item--right" style="top:254px"><div class="name">Negroni</div><p class="desc">Camporosso, Gin, Vallato Vermouth di Torino,<br>Orangenscheibe <span class="price" style="margin-left:4px">9.90</span></p></div>
  <div class="item item--right" style="top:288px"><div class="name">Grand Ginger</div><p class="desc">Grand Orangier, Ginger Ale, Limettensaft,<br>Orangenscheibe <span class="vol">0,2l</span><span class="price">9.90</span></p></div>
  <div class="label-bold" style="left:299px;top:333px;transform:translateX(-50%);left:320px">Alkoholfrei</div>
  <div class="item item--right" style="top:356px"><div class="name">Hugo alkoholfrei</div><p class="desc">Ginger Ale, Holundersirup, Limette, Pfefferminz<br><span class="vol">0,2l</span><span class="price">7.50</span></p></div>
  <div class="item item--right" style="top:390px"><div class="name">Black Hugo alkoholfrei</div><p class="desc">Holundersirup, Johannisbeersaft<br><span class="vol">0,2l</span><span class="price">7.50</span></p></div>
  <div class="item item--right" style="top:424px"><div class="name">Lisette Wild Berry alkoholfrei</div><p class="desc">Dark Wild Berry, Mineralwasser, Beeren<br>Pfefferminz <span class="vol">0,2l</span><span class="price">7.90</span></p></div>

  <div class="brand" style="top:473px">Casa Vittoria</div>
  <div class="tricolore" style="top:506px"><i class="g"></i><i class="w"></i><i class="r"></i></div>
</section>

<!-- Soups and starters page -->
<section class="page page--food">
  <div class="title-block" style="top:68px"><h2 class="title"><span class="initial">S</span>uppen</h2></div>
  <div class="photo photo--soup" role="img" aria-label="Foto einer Tomatensuppe in roter Schale"></div>

  <div class="item item--dish" style="left:108px;top:126px;width:174px"><div class="name">Tomatensuppe <sup>G</sup></div><p class="desc">Mit Sahnehäubchen aufwartend</p><span class="price" style="top:10px">6.60</span></div>
  <div class="item item--dish" style="left:108px;top:151px;width:174px"><div class="name">Minestrone</div><p class="desc">Mit frischem Gemüse</p><span class="price" style="top:10px">6.90</span></div>
  <div class="item item--dish" style="left:108px;top:176px;width:174px"><div class="name">Tortellini in Brodo <sup>L</sup></div><p class="desc">Hackfleisch gefüllte Tortellini<br>in kräftiger Brühe</p><span class="price" style="top:10px">6.90</span></div>
  <div class="item item--dish" style="left:108px;top:208px;width:174px"><div class="name">Italienische Zwiebelsuppe <sup>G</sup></div><p class="desc">Die feine hausgemachte Suppe erreicht Sie<br>frisch aus dem Ofen mit einer knusprigen<br>Pizzateighaube</p><span class="price" style="top:10px">9.50</span></div>

  <div class="title-block" style="top:259px"><h2 class="title"><span class="initial">A</span>ntipasti</h2></div>
  <div class="photo photo--caprese" role="img" aria-label="Foto eines Tellers Caprese mit Tomate und Mozzarella"></div>

  <div class="item item--dish" style="left:15px;top:332px;width:170px"><div class="name">Gebackener Schafskäse mit Salat <sup>G</sup></div><p class="desc">Panierter und frittierter Schafskäse<br>an Salatbouquet</p><span class="price">13.90</span></div>
  <div class="item item--dish" style="left:15px;top:366px;width:170px"><div class="name">Carpaccio di Manzo <sup>G,L</sup></div><p class="desc">Hauchfein geschnittene Rinderfilet-Scheiben<br>auf Rucolabett. Mit frischen Champignons,<br>Parmesankäse &amp; Sellerie</p><span class="price">15.90</span></div>
  <div class="item item--dish" style="left:15px;top:408px;width:170px"><div class="name">Garnelen-Pfännchen <sup>B</sup></div><p class="desc">Leckere gebratene Garnelen in mit Knoblauch<br>und Kräutern abgeschmeckter Soße</p><span class="price">16.90</span></div>
  <div class="item item--dish" style="left:15px;top:440px;width:170px"><div class="name">Vitello Tonnato <sup>6,D,G</sup></div><p class="desc">Fein geschnittener Kalbsbraten bedeckt mit<br>Thunfischcreme, angemacht mit Oliven,<br>Kapern &amp; Sardellen</p><span class="price" style="top:19px">14.50</span></div>

  <div class="item item--dish" style="left:206px;top:332px;width:156px"><div class="name">Insalata di Mare <sup>B,D,R</sup></div><p class="desc">Hausgemachter Meeresfrüchte-Salat<br>erwartet Sie hier.<br>Dazu reichen wir Ihnen Brot</p><span class="price">15.90</span></div>
  <div class="item item--dish" style="left:206px;top:373px;width:156px"><div class="name">Antipasto Misto <sup>6,B,D,G,R</sup></div><p class="desc">Genießen Sie eine von unserem Küchen-<br>chef zusammengestellte leckere<br>Kombination kalt-warmer Vorspeisen-<br>Spezialitäten aus mediterranen Gefilden</p><span class="price">15.90</span></div>
  <div class="item item--dish" style="left:206px;top:419px;width:156px"><div class="name">Caprese <sup>G</sup></div><p class="desc">Italienische Vorspeisen-Spezialität u.a. aus<br>Tomatenscheiben, Mozzarella-Käse<br>und Basilikum</p><span class="price">9.90</span></div>

  <div class="brand" style="top:473px">Casa Vittoria</div>
  <div class="tricolore" style="top:507px"><i class="g"></i><i class="w"></i><i class="r"></i></div>
</section>

<!-- Drinks page -->
<section class="page page--drinks">
  <div class="title-block" style="top:68px"><h2 class="title"><span class="initial">G</span>etränke</h2></div>

  <div class="script-head" style="left:16px;top:137px">Alkoholfrei</div>
  <span class="vol-head" style="left:126px;top:159px">0,2l</span>
  <span class="vol-head" style="left:170px;top:159px">0,4l</span>
  <div class="row" style="top:171px"><span class="dname" style="left:16px">Kolara <sup>1,9,17</sup></span><span class="p" style="left:127px">2.90</span><span class="p" style="left:171px">4.70</span></div>
  <div class="row" style="top:188px"><span class="dname" style="left:16px">Kolara light <sup>1,9,11,12</sup></span><span class="p" style="left:127px">2.90</span><span class="p" style="left:171px">4.70</span></div>
  <div class="row" style="top:204px"><span class="dname" style="left:16px">Aranella <sup>1,G</sup></span><span class="p" style="left:127px">2.90</span><span class="p" style="left:171px">4.70</span></div>
  <div class="row" style="top:220px"><span class="dname" style="left:16px">Limora</span><span class="p" style="left:127px">2.90</span><span class="p" style="left:171px">4.70</span></div>
  <div class="row" style="top:237px"><span class="dname" style="left:16px">Kolamix <sup>1,9,17,G</sup></span><span class="p" style="left:127px">2.90</span><span class="p" style="left:171px">4.70</span></div>

  <div class="script-head" style="left:19px;top:256px">Fruchtig</div>
  <span class="vol-head" style="left:126px;top:277px">0,2l</span>
  <span class="vol-head" style="left:170px;top:277px">0,4l</span>
  <div class="row" style="top:289px"><span class="dname" style="left:16px">Apfelsaft</span><span class="p" style="left:127px">2.90</span><span class="p" style="left:171px">4.70</span></div>
  <div class="row" style="top:305px"><span class="dname" style="left:16px">Apfelsaft-Schorle</span><span class="p" style="left:127px">2.90</span><span class="p" style="left:171px">4.70</span></div>
  <div class="row" style="top:322px"><span class="dname" style="left:16px">Orangensaft</span><span class="p" style="left:127px">2.90</span><span class="p" style="left:171px">4.70</span></div>
  <div class="row" style="top:338px"><span class="dname" style="left:16px">Kirschnektar</span><span class="p" style="left:127px">2.90</span><span class="p" style="left:171px">4.70</span></div>
  <div class="row" style="top:354px"><span class="dname" style="left:16px">Orangensaft</span><span class="p" style="left:127px">2.90</span><span class="p" style="left:171px">4.70</span></div>
  <div class="row" style="top:371px"><span class="dname" style="left:16px">Kirschnektar</span><span class="p" style="left:127px">2.90</span><span class="p" style="left:171px">4.70</span></div>
  <div class="row" style="top:387px"><span class="dname" style="left:16px">Kirschnektar</span><span class="p" style="left:127px">2.90</span><span class="p" style="left:171px">4.70</span></div>

  <div class="script-head" style="left:19px;top:411px">Eistee</div>
  <div class="row" style="top:444px"><span class="dname" style="left:16px">Sun Harbor Eistee</span><span class="vol-head" style="left:175px;top:2px">0,33l</span></div>
  <div class="row" style="top:460px"><span class="dname" style="left:22px">Pfirsich</span><span class="p" style="left:171px">5.20</span></div>
  <div class="row" style="top:476px"><span class="dname" style="left:22px">Zitrone</span><span class="p" style="left:171px">5.20</span></div>

  <div class="script-head" style="left:211px;top:137px">Wasser</div>
  <span class="vol-head" style="left:302px;top:159px">0,25l</span>
  <span class="vol-head" style="left:347px;top:159px">0,75l</span>
  <div class="row" style="top:171px"><span class="dname" style="left:211px">San Valerio</span><span class="p" style="left:303px">2.80</span><span class="p" style="left:346px">6.50</span></div>
  <div class="row" style="top:188px"><span class="dname" style="left:211px">Fontelli Still</span><span class="p" style="left:303px">2.90</span><span class="p" style="left:346px">6.90</span></div>
  <div class="row" style="top:204px"><span class="dname" style="left:211px">Fontelli</span><span class="p" style="left:303px">2.90</span><span class="p" style="left:346px">6.90</span></div>

  <div class="script-head" style="left:212px;top:253px">Erfrischend</div>
  <span class="vol-head" style="left:307px;top:278px">0,2l</span>
  <span class="vol-head" style="left:352px;top:278px">0,4l</span>
  <div class="row" style="top:290px"><span class="dname" style="left:212px">Bitter Lemon <sup>3,10</sup></span><span class="p" style="left:303px">3.20</span><span class="p" style="left:346px">5.10</span></div>
  <div class="row" style="top:306px"><span class="dname" style="left:212px">Ginger Ale <sup>1</sup></span><span class="p" style="left:303px">3.20</span><span class="p" style="left:346px">5.10</span></div>
  <div class="row" style="top:323px"><span class="dname" style="left:212px">Tonic Water <sup>10</sup></span><span class="p" style="left:303px">3.30</span><span class="p" style="left:346px">5.30</span></div>

  <span class="vol-head" style="left:307px;top:392px">0,2l</span>
  <div class="row" style="top:404px"><span class="dname" style="left:212px">H-Milch</span><span class="p" style="left:303px">2.20</span></div>

  <div class="brand" style="top:469px">Casa Vittoria</div>
  <div class="tricolore" style="top:507px"><i class="g"></i><i class="w"></i><i class="r"></i></div>
</section>

</body>
</html>
```